Real Estate Broker specializing in investment property needs business card

Would like to use a tag line for my company, Larkmoor Keys LLC (Right now I use Larkmoor Keys - For Real Estate Needs). I you have a more creative tag line it can be used because this is a new company.
We focus on Investment Acquisition Deals; Provide Custom Marketing Strategies for Sellers; Provide Pre Listinging Value Opportunities for Buyers.
Would like a call to action, but I do not want it to look too cluttered
I would like space to be available for writing on.
I prefer vertical business cards, but it could be horizontal on one or both sides. In fact if you can create a shape other than rectangle or a cut in the rectangle that makes it memorable, relevant to real estate, yet practical...(it will be kept) that would be of value.
If you have experience with business cards please feel free to suggest the paper type, size.

Target Market(s)

Investors, Neighbors, Friends... anyone who buys or would like to sell their residence

Industry/Entity Type

Real Estate

Contact Information for Business Card

The challenge is to incorporate a logo design of the Managing Brokerage Company, Tiller's Circle, and try to brand my company, LarkmoorKeys LLC. LarkmoorKeys LLC could work under another managing broker but the services and contact information would remain the same.

Font styles to use
Serif

Colors

Designer to choose colors to be used in the design.

Requirements
Must have
• Real estate company named Larkmoor Keys has to incorporate the logo of the managing broker company, Tillers Circle (see attached) into design of business card. (It is not a design for a logo I prefer but I need to use it. Size does not matter).
• Must also have my name, phone number and email address. (No website address yet)
• Just a few of the services we provide include
• We facilitate Investment Acquisition Deals; Provide Custom Marketing Strategies for Sellers; Provide Pre Listinging Value Opportunities for Buyers.
Nice to have
• Would like to use a tag line for my company, Larkmoor Keys LLC (Right now I use Larkmoor Keys - For Real Estate Needs). If you have a more creative tag line it can be used because this is a new company.
• Space to write information on, so they keep the card such as an appointment time to sit down and determine their needs
• A call to action maybe after the services? Or on the back of the card where it is blank.
• Larkmoor Keys does not have a logo, If you think a logo for Tillers Circle and a logo for LarkmoorKeys LLC can work, then please incorporate it into the business card.
Should not have
• Clutter
• Do not like comic style designs; prefer a sophisticated look and texture.

```html
<!DOCTYPE html>
<html lang="en">
<head>
<meta charset="utf-8">
<title>Larkmoor Keys LLC – Business Card</title>
<link rel="stylesheet" href="https://fonts.googleapis.com/css2?family=Cinzel:wght@400;500&family=Lato:wght@400&display=swap">
<style>
  :root {
    --backdrop: #3b3b3b;
    --card-black: #000000;
    --card-light: #f5f5f5;
    --brand-red: #c0162c;
    --band-red: #a51515;
    --text-white: #ffffff;
    --text-soft: #cfcfcf;
    --mark-grey: #8a8a8a;
    --faint-grey: #e2e2e2;
    --accent-gold: #e8a21c;
    --badge-red: #8e1024;
  }
  * { margin: 0; padding: 0; box-sizing: border-box; }
  html, body { width: 1200px; height: 900px; overflow: hidden; }
  body { background: var(--backdrop); position: relative; font-family: "Lato", Arial, sans-serif; }

  .card { position: absolute; box-shadow: 2px 3px 6px rgba(0,0,0,.45); }

  .card-front {
    left: 243px; top: 200px; width: 310px; height: 502px;
    background: var(--card-black); color: var(--text-white);
    text-align: center;
  }
  .agent-name {
    position: absolute; top: 55px; left: 0; right: 0;
    font-family: "Cinzel", Georgia, serif; font-weight: 400;
    font-size: 19px; letter-spacing: 0.5px;
    color: var(--brand-red);
  }
  .contact-block {
    position: absolute; top: 100px; left: 0; right: 0;
    font-size: 16px; line-height: 20.5px;
  }
  .contact-block .gap { height: 19px; }
  .tagline {
    position: absolute; top: 254px; left: 0; right: 0;
    font-family: "Cinzel", Georgia, serif; color: var(--brand-red);
    font-size: 21px; line-height: 27px; letter-spacing: 1px;
  }
  .tagline .company { font-size: 25px; }
  .brand-mark {
    position: absolute; top: 372px; left: 0; right: 0;
    display: flex; align-items: center; justify-content: center; gap: 10px;
    font-family: "Cinzel", Georgia, serif; font-size: 22px; color: var(--mark-grey);
  }
  .brand-mark .square { width: 16px; height: 16px; background: var(--brand-red); }
  .services {
    position: absolute; top: 414px; left: 20px; right: 20px;
    list-style: none; font-size: 11.5px; line-height: 15px; color: var(--text-soft);
  }
  .call-to-action {
    position: absolute; top: 466px; left: 0; right: 0;
    font-family: "Cinzel", Georgia, serif; font-size: 11.5px; letter-spacing: 0.5px;
    color: var(--accent-gold);
  }

  .card-back {
    left: 588px; top: 392px; width: 501px; height: 310px;
    background: var(--card-light); text-align: center;
  }
  .company-wordmark {
    position: absolute; top: 64px; left: 0; right: 0;
    font-family: "Cinzel", Georgia, serif; color: var(--faint-grey);
    font-size: 58px; line-height: 70px; letter-spacing: 3px;
  }
  .company-sub {
    position: absolute; top: 134px; left: 50px; right: 50px;
    display: flex; align-items: center; gap: 14px;
    font-family: "Cinzel", Georgia, serif; color: var(--faint-grey);
    font-size: 34px; letter-spacing: 3px;
  }
  .company-sub .rule { flex: 1; height: 1px; background: var(--faint-grey); }
  .member-label {
    position: absolute; top: 194px; left: 0; right: 0;
    font-size: 15px; color: var(--accent-gold);
  }
  .partner-badge { position: absolute; top: 216px; left: 180px; }
  .red-band {
    position: absolute; left: 0; right: 0; bottom: 0; height: 16px;
    background: var(--band-red);
  }
</style>
</head>
<body>
  <section class="card card-front">
    <h1 class="agent-name">DESMOND WHITCOMBE</h1>
    <div class="contact-block">
      <p>418 Alder Crest Avenue</p>
      <p>Suite 212</p>
      <p>Fairhollow, Colorado 80999</p>
      <div class="gap"></div>
      <p>555.014.2278</p>
      <p>des@larkmoorkeys.com</p>
    </div>
    <p class="tagline"><span class="company">LarkmoorKeys</span><br>FOR YOUR<br>REAL ESTATE NEEDS</p>
    <div class="brand-mark"><span class="square"></span><span>Larkmoor Keys</span></div>
    <ul class="services">
      <li>Investment Acquisition Deals</li>
      <li>Custom Marketing Strategies for Sellers</li>
      <li>Pre-Listing Value Opportunities for Buyers</li>
    </ul>
    <p class="call-to-action">Call today to book your consultation</p>
  </section>

  <section class="card card-back">
    <p class="company-wordmark">LARKMOOR</p>
    <div class="company-sub"><span class="rule"></span><span>KEYS LLC</span><span class="rule"></span></div>
    <p class="member-label">MEMBER OF</p>
    <svg class="partner-badge" width="141" height="52" viewBox="0 0 141 52" role="img" aria-label="Tillers Circle partner badge">
      <ellipse cx="70.5" cy="26" rx="68" ry="24" fill="var(--badge-red)" stroke="var(--accent-gold)" stroke-width="3"/>
    </svg>
    <div class="red-band"></div>
  </section>
</body>
</html>
```